Flyer for the Radiant Harvest Worship Day

I am looking to create a flyer for a one day prayer retreat our church is organizing.
This flyer will be posted on social media, websites and will also be printed so it can be mailed to people.
I am looking for something professional, with good use of our logo and band colors (logo colors).
I am counting on the designer's skill, creativity, art and knowledge of media communication to produce a flyer that will effectively and quickly convey the message we are trying to spread.
CONTENT OF THE FLYER:
Event title: Radiant Harvest Worship Day
Date: Tuesday July 2nd, 2019
Time: 11:00AM - 7:00PM
Belmont Hotel, 4875 Maple Ridge Road, Portland, Maine 04219 (Room: Evergreen)
Event Key words to highlight what the event is about: Prayer, Sharing the Word, Panel discussion, prophecy, Impartation.
Key phrases:
A one day prayer retreat.
Jesus Chris is Lord
Contact info:
www.tuvela.org
Phone: 207 583 2194
Email: contact@brookmeadow.org

```html
<!DOCTYPE html>
<html lang="en">
<head>
<meta charset="utf-8">
<title>Radiant Harvest Worship Day</title>
<link rel="stylesheet" href="https://fonts.googleapis.com/css2?family=Cinzel:wght@400;600;700&family=Lato:ital,wght@0,400;0,700;1,700&display=swap">
<style>
  :root {
    --navy: #15355f;
    --navy-deep: #0f2f57;
    --orange: #f18a22;
    --orange-light: #fbb731;
    --ink: #1d2f4f;
    --paper: #ffffff;
    --mist: #eef0f3;
    --photo-dark: #2c2c2c;
    --photo-mid: #8d8d8d;
    --photo-light: #d9d9d9;
  }
  * { margin: 0; padding: 0; box-sizing: border-box; }
  html, body { width: 1200px; height: 902px; overflow: hidden; background: var(--paper); }
  .flyer {
    position: relative; width: 1200px; height: 902px; overflow: hidden;
    font-family: "Lato", Arial, sans-serif; color: var(--ink);
    background: var(--paper);
  }
  .backdrop-photo {
    position: absolute; left: 520px; top: 0; width: 680px; height: 902px;
    background: linear-gradient(120deg, #ffffff 0%, var(--mist) 45%, #f7f7f8 75%, #e9eaed 100%);
  }
  .hands-photo {
    position: absolute; left: 0; top: 0; width: 640px; height: 740px;
    background: radial-gradient(ellipse at 40% 55%, var(--photo-light) 0%, var(--photo-mid) 45%, var(--photo-dark) 90%);
    -webkit-mask-image: linear-gradient(90deg, #000 0%, #000 72%, transparent 100%);
    mask-image: linear-gradient(90deg, #000 0%, #000 72%, transparent 100%);
  }
  .shapes { position: absolute; left: 0; top: 0; }
  .brand {
    position: absolute; left: 150px; top: 118px;
    display: flex; align-items: center; gap: 14px;
  }
  .brand-dot { width: 26px; height: 26px; border-radius: 50%; background: var(--orange); }
  .brand-name {
    font-family: "Cinzel", Georgia, serif; font-weight: 600; font-size: 66px;
    color: var(--navy); letter-spacing: 1px; line-height: 1;
  }
  .event {
    position: absolute; left: 634px; top: 58px; width: 500px; text-align: center;
  }
  .event-title { font-family: "Cinzel", Georgia, serif; font-weight: 600; line-height: 1; white-space: nowrap; }
  .event-title .line-one { display: block; font-size: 50px; color: var(--navy); }
  .event-title .line-two { display: block; font-size: 66px; color: var(--orange); margin-top: 4px; margin-left: -30px; margin-right: -30px; }
  .label-rule {
    display: flex; align-items: center; gap: 10px; margin-top: 14px;
    font-family: "Cinzel", Georgia, serif; font-size: 17px; color: var(--orange);
  }
  .label-rule::before, .label-rule::after {
    content: ""; flex: 1; height: 3px;
    background: linear-gradient(90deg, var(--navy), #7fa3d4);
  }
  .event-date { font-family: "Cinzel", Georgia, serif; font-size: 40px; color: var(--ink); margin-top: 6px; white-space: nowrap; }
  .event-time { font-family: "Cinzel", Georgia, serif; font-size: 26px; font-weight: 700; color: var(--ink); margin-top: 2px; }
  .pin { display: block; margin: 14px auto 0; }
  .venue { font-size: 19px; line-height: 25px; color: var(--ink); margin-top: 12px; white-space: nowrap; }
  .topics { position: absolute; left: 0; top: 0; }
  .topic { position: absolute; width: 170px; text-align: center; font-size: 19px; line-height: 24px; color: var(--ink); }
  .topic svg { display: block; margin: 0 auto 6px; }
  .tagline {
    position: absolute; left: 644px; top: 754px; width: 556px; height: 62px;
    background: var(--orange); display: flex; align-items: center; padding-left: 24px;
    font-style: italic; font-weight: 700; font-size: 23px; color: var(--navy-deep);
  }
  .tagline .emphasis { color: #ffffff; margin-left: 6px; }
  .contact { position: absolute; left: 0; top: 742px; width: 680px; height: 160px; color: #ffffff; }
  .visit { position: absolute; left: 74px; top: 14px; font-size: 17px; font-weight: 700; color: var(--orange-light); }
  .website { position: absolute; left: 74px; top: 42px; font-size: 23px; display: flex; align-items: center; gap: 8px; }
  .divider { position: absolute; left: 294px; top: 0; width: 2px; height: 72px; background: #ffffff; }
  .phone { position: absolute; left: 329px; top: 0; font-size: 32px; font-weight: 700; display: flex; align-items: center; gap: 10px; }
  .email { position: absolute; left: 329px; top: 44px; font-size: 21px; display: flex; align-items: center; gap: 10px; }
</style>
</head>
<body>
<main class="flyer">
  <div class="backdrop-photo" role="img" aria-label="Faint photograph of hands folded in prayer"></div>
  <div class="hands-photo" role="img" aria-label="Black and white photograph of folded hands resting on a Bible with a cross"></div>

  <svg class="shapes" width="1200" height="902" viewBox="0 0 1200 902" aria-hidden="true">
    <path d="M0 700 C220 702 430 682 560 652 C630 635 675 612 700 588 C688 690 680 800 690 902 L0 902 Z" fill="var(--orange)"/>
    <path d="M0 714 C220 716 430 696 560 666 C630 649 675 626 700 602 C688 700 680 800 690 902 L0 902 Z" fill="#ffffff"/>
    <path d="M0 722 C220 724 430 704 560 674 C630 657 675 634 700 610 C688 706 680 806 690 902 L0 902 Z" fill="var(--navy-deep)"/>
  </svg>

  <div class="brand">
    <span class="brand-dot"></span>
    <span class="brand-name">TUVELA</span>
  </div>

  <section class="event">
    <h1 class="event-title">
      <span class="line-one">RADIANT HARVEST</span>
      <span class="line-two">WORSHIP DAY</span>
    </h1>
    <div class="label-rule">DATE</div>
    <p class="event-date">TUESDAY JULY 2ND, 2019</p>
    <div class="label-rule">TIME</div>
    <p class="event-time">11:00AM - 7:00PM</p>
    <svg class="pin" width="38" height="38" viewBox="0 0 38 38" aria-hidden="true">
      <circle cx="19" cy="19" r="17" fill="#ffffff" stroke="var(--navy)" stroke-width="2"/>
      <path d="M19 9 C14.5 9 12 12.2 12 15.6 C12 20 19 28 19 28 C19 28 26 20 26 15.6 C26 12.2 23.5 9 19 9 Z" fill="var(--orange)"/>
      <circle cx="19" cy="15.8" r="2.8" fill="#ffffff"/>
    </svg>
    <p class="venue">Belmont Hotel, 4875 Maple Ridge Road, Portland,<br>Maine 04219 (Room: Evergreen)</p>
  </section>

  <div class="topics">
    <div class="topic" style="left:669px;top:496px">
      <svg width="70" height="70" viewBox="0 0 72 72" aria-hidden="true"><circle cx="36" cy="36" r="35" fill="var(--navy)"/><circle cx="36" cy="36" r="31" fill="var(--orange)"/><path d="M36 20 V38 M29 26 H43" stroke="#fff" stroke-width="3"/><path d="M22 46 L30 40 L36 48 L42 40 L50 46" fill="none" stroke="#fff" stroke-width="3" stroke-linejoin="round"/></svg>
      Prayer
    </div>
    <div class="topic" style="left:815px;top:496px">
      <svg width="70" height="70" viewBox="0 0 72 72" aria-hidden="true"><circle cx="36" cy="36" r="35" fill="var(--navy)"/><circle cx="36" cy="36" r="31" fill="var(--orange)"/><circle cx="36" cy="24" r="4" fill="#fff"/><circle cx="24" cy="32" r="4" fill="#fff"/><circle cx="48" cy="32" r="4" fill="#fff"/><path d="M30 50 V34 H42 V50 M18 50 V42 H30 M42 42 H54 V50" fill="none" stroke="#fff" stroke-width="3"/></svg>
      Sharing the<br>Word
    </div>
    <div class="topic" style="left:977px;top:496px">
      <svg width="70" height="70" viewBox="0 0 72 72" aria-hidden="true"><circle cx="36" cy="36" r="35" fill="var(--navy)"/><circle cx="36" cy="36" r="31" fill="var(--orange)"/><rect x="20" y="18" width="14" height="9" fill="#fff"/><rect x="38" y="18" width="14" height="9" fill="#fff"/><rect x="20" y="40" width="32" height="12" fill="#fff"/><circle cx="26" cy="34" r="3" fill="#fff"/><circle cx="36" cy="34" r="3" fill="#fff"/><circle cx="46" cy="34" r="3" fill="#fff"/></svg>
      Panel<br>discussion
    </div>
    <div class="topic" style="left:706px;top:634px">
      <svg width="70" height="70" viewBox="0 0 72 72" aria-hidden="true"><circle cx="36" cy="36" r="35" fill="var(--navy)"/><circle cx="36" cy="36" r="31" fill="var(--orange)"/><circle cx="36" cy="36" r="16" fill="none" stroke="#fff" stroke-width="3"/><path d="M36 18 V54 M30 28 H42" stroke="#fff" stroke-width="3"/></svg>
      Prophecy
    </div>
    <div class="topic" style="left:900px;top:634px">
      <svg width="70" height="70" viewBox="0 0 72 72" aria-hidden="true"><circle cx="36" cy="36" r="35" fill="var(--navy)"/><circle cx="36" cy="36" r="31" fill="var(--orange)"/><rect x="24" y="30" width="24" height="20" fill="none" stroke="#fff" stroke-width="3"/><rect x="21" y="24" width="30" height="7" fill="#fff"/><path d="M36 24 V50" stroke="#fff" stroke-width="3"/><path d="M36 24 C32 16 26 18 30 23 M36 24 C40 16 46 18 42 23" fill="none" stroke="#fff" stroke-width="2"/></svg>
      Impartation
    </div>
  </div>

  <div class="tagline">A one day prayer retreat.<span class="emphasis">Jesus Chris is Lord</span></div>

  <footer class="contact">
    <p class="visit">Visit Us today!</p>
    <p class="website">
      <svg width="18" height="18" viewBox="0 0 18 18" aria-hidden="true"><circle cx="9" cy="9" r="7.5" fill="none" stroke="var(--orange-light)" stroke-width="1.6"/><ellipse cx="9" cy="9" rx="3.2" ry="7.5" fill="none" stroke="var(--orange-light)" stroke-width="1.4"/><path d="M1.5 9 H16.5" stroke="var(--orange-light)" stroke-width="1.4"/></svg>
      www.tuvela.org
    </p>
    <span class="divider"></span>
    <p class="phone">
      <svg width="24" height="24" viewBox="0 0 24 24" aria-hidden="true"><circle cx="12" cy="12" r="10.5" fill="none" stroke="var(--orange-light)" stroke-width="1.8"/><path d="M8.5 7 L10.5 7 L11 9.5 L9.8 10.4 C10.5 12 11.8 13.3 13.4 14 L14.3 12.8 L16.8 13.3 L16.8 15.3 C12 15.8 8 11.8 8.5 7 Z" fill="var(--orange-light)"/></svg>
      207 583 2194
    </p>
    <p class="email">
      <svg width="24" height="18" viewBox="0 0 24 18" aria-hidden="true"><rect x="1" y="1" width="22" height="16" fill="var(--orange-light)"/><path d="M1 1 L12 10 L23 1" fill="none" stroke="var(--navy-deep)" stroke-width="1.8"/></svg>
      contact@brookmeadow.org
    </p>
  </footer>
</main>
</body>
</html>
```